Create a Brochure Design for Brantley Homecare

Brantley Homecare is a subsidiary of the Brantley Care Group. This brochure is specifically for the Brantley Homecare company and brand. Create a 3 panel, A4, front and back, tri-fold brochure. This brochure will be a way to introduce our Homecare services to the community, prospective clients, and various referral partners. The brochure must be eye catching, unique in its deliverables and demonstrate both attention to detail and comfort. Our organization is sophisticated and built around warmth, care and individualized personal attention. The most important aspect of this design is to focus on creating a nurturing, warm, and inviting feel where you would want to have a Nurse or Nurse’s Aide in your own home or a loved one’s home.

I am open to the creativity of the designer to develop something based on the above criteria; however I would like the design to work well with the existing collateral material. What I mean by that is that while I want everything to have its own personality and stand out as its own brand representative, I still need to be able to tell that the overall design concept stays stylistically inside of the same ‘family’ of existing designed material. Because of this, below I would like for the designer to pull inspiration from the link to our website (Located below) as well as from the attachment of our recently refreshed business cards (Attached). This should allow each design to be unique and creative, while still staying inside of a framework and the feel/style that I am looking for.

Finally, I want all the designers to understand that this brochure design is for a private, in home, healthcare company where we are responsible for providing personalized care for a culturally and ethnically diverse make-up clientele of all ages. The photos that are used must represent an image of warmth, care, and a positive interaction between client and caregiver.

Look under the Brantley Homecare tab at www.brantleycaregroup-example.net

Industry/Entity Type

Healthcare

Requirements
Must have
• • The Brantley Homecare company logo must be included.

```html
<!DOCTYPE html>
<html lang="en">
<head>
<meta charset="utf-8">
<title>Brantley Homecare – Tri-fold Brochure</title>
<link rel="stylesheet" href="https://fonts.googleapis.com/css2?family=Open+Sans:wght@300;400;600;700&display=swap">
<style>
  :root {
    --green: #1f8a4d;
    --green-dark: #17703d;
    --pink: #ef8589;
    --pink-soft: #f6b3b2;
    --cream: #f3f0e6;
    --mint: #d5e8cb;
    --ink: #3a3a3a;
    --grey: #6d6d6d;
    --white: #ffffff;
    --photo-skin: #d9c2ad;
    --photo-blue: #a9cbe0;
    --photo-warm: #e4d6c4;
  }
  * { box-sizing: border-box; margin: 0; padding: 0; }
  html, body { width: 1200px; height: 425px; overflow: hidden; background: var(--white); }
  body { font-family: "Open Sans", Arial, sans-serif; color: var(--ink); }
  .canvas { position: relative; width: 1200px; height: 425px; overflow: hidden; background: var(--white); }

  .spread { position: absolute; top: 13px; height: 398px; background: var(--cream); overflow: hidden; }
  .spread--outside { left: 11px; width: 576px; }
  .spread--inside { left: 607px; width: 573px; }

  .abs { position: absolute; }
  .photo { position: absolute; }
  .shape { position: absolute; display: block; }

  .heading { font-size: 5.6px; font-weight: 700; letter-spacing: .2px; color: var(--ink); margin-bottom: 3px; }
  .body-copy { font-size: 5px; line-height: 1.45; color: var(--grey); margin-bottom: 6px; }
  .on-color .heading, .on-color .body-copy { color: var(--white); }

  .brand { display: flex; align-items: center; gap: 4px; color: var(--green); font-weight: 600; white-space: nowrap; }
  .brand__dot { width: 9px; height: 9px; border-radius: 50%; background: var(--pink); flex: none; }
  .brand--light { color: var(--white); }
  .brand--light .brand__dot { background: var(--white); }

  .tagline { font-size: 4.6px; color: var(--green); font-style: normal; text-align: center; line-height: 1.4; }

  /* outside panel 1 */
  .lead-band { left: 0; top: 200px; width: 192px; height: 48px; background: var(--mint); }
  /* outside panel 2 */
  .contact { left: 215px; top: 346px; width: 150px; font-size: 5px; line-height: 1.5; color: var(--ink); }
  .contact strong { font-weight: 700; font-size: 5.4px; }
  /* outside panel 3 */
  .cover-title { left: 490px; top: 205px; width: 80px; font-size: 12px; line-height: 1.2; font-weight: 300; color: var(--white); }

  /* inside */
  .headline { left: 7px; top: 4px; width: 230px; font-size: 16px; line-height: 1.2; font-weight: 300; color: var(--grey); }
  .column { top: 218px; }
</style>
</head>
<body>
<div class="canvas">

  <!-- OUTSIDE SPREAD -->
  <section class="spread spread--outside" aria-label="Brochure outside">
    <!-- panel 1 -->
    <div class="photo" role="img" aria-label="Photo of a caregiver in blue scrubs with a fob watch" style="left:0;top:0;width:192px;height:200px;background:linear-gradient(135deg,var(--photo-blue),#e9eef1 60%,var(--photo-skin));"></div>
    <svg class="shape" style="left:142px;top:0" width="50" height="60" viewBox="0 0 50 60"><polygon points="0,0 50,0 50,60" fill="var(--pink)" opacity=".85"/></svg>
    <div class="abs lead-band"></div>
    <div class="abs" style="left:9px;top:206px;width:176px;">
      <p class="heading">LOREM IPSUM DOLOR SIT AMET</p>
      <p class="body-copy">Consectetur adipiscing elit. In eu hendrerit dolor. Nullam sodales nunc quis arcu dignissim interdum. Vivamus lobortis metus vel ligula euismod a pharetra mi pharetra.</p>
      <p class="body-copy" style="width:110px">Consectetur adipiscing elit. In eu hendrerit dolor. Nullam sodales nunc quis arcu dignissim interdum. Vivamus lobortis metus vel ligula euismod a pharetra mi pharetra.</p>
    </div>
    <svg class="shape" style="left:118px;top:284px" width="74" height="70" viewBox="0 0 74 70"><polygon points="74,0 74,70 0,70" fill="var(--green)"/></svg>
    <svg class="shape" style="left:0;top:340px" width="60" height="58" viewBox="0 0 60 58"><polygon points="0,0 60,58 0,58" fill="var(--pink)"/></svg>
    <div class="abs" style="left:6px;top:352px;width:48px;">
      <div class="brand" style="font-size:6px;flex-direction:column;gap:2px;"><span class="brand__dot"></span>Brantley Homecare</div>
    </div>
    <p class="abs body-copy" style="left:70px;top:372px;width:110px;">Fusce aliquam, quam ut pulvinar scelerisque, justo mi mi, eget. Morbi hac nulla quisque euismod dolor mollis.</p>

    <!-- panel 2 -->
    <div class="abs" style="left:192px;top:0;width:192px;height:398px;background:var(--cream);"></div>
    <div class="abs" style="left:192px;top:168px;width:192px;display:flex;flex-direction:column;align-items:center;">
      <span class="brand__dot" style="width:14px;height:14px;margin-bottom:5px;"></span>
      <div class="brand" style="font-size:15px;">Brantley Homecare</div>
      <p class="tagline" style="margin-top:4px;">Someone you can depend on...<br>Without question.</p>
    </div>
    <address class="abs contact" style="font-style:normal;">
      <strong>BRANTLEY HOMECARE</strong><br>
      480 Meadowlark Ave<br>
      Suite #210, Lakemont, OR 97000<br>
      Phone: 555-014-2286<br>
      Fax: 555-014-2290<br>
      <strong>info@brantleycare-example.com</strong>
    </address>

    <!-- panel 3 -->
    <div class="abs" style="left:466px;top:0;width:62px;height:88px;background:var(--green);"></div>
    <div class="abs" style="left:468px;top:24px;width:58px;display:flex;flex-direction:column;align-items:center;">
      <div class="brand brand--light" style="font-size:6px;flex-direction:column;gap:3px;"><span class="brand__dot"></span>Brantley</div>
      <p class="tagline" style="color:var(--white);margin-top:3px;">Homecare</p>
    </div>
    <div class="photo" role="img" aria-label="Photo of a nurse smiling beside an elderly woman" style="left:392px;top:120px;width:74px;height:112px;background:linear-gradient(160deg,#ece5da,var(--photo-skin) 70%,#c8a88f);"></div>
    <svg class="shape" style="left:466px;top:120px" width="110" height="150" viewBox="0 0 110 150"><polygon points="0,0 110,80 110,150 0,150" fill="var(--pink)"/></svg>
    <svg class="shape" style="left:440px;top:120px" width="54" height="70" viewBox="0 0 54 70"><polygon points="0,0 54,0 54,70" fill="var(--green)" opacity=".0"/></svg>
    <p class="abs cover-title">Lorem ipsum dolor sit amet adipiscing elit</p>
    <div class="photo" role="img" aria-label="Photo of a caregiver walking with a senior woman" style="left:500px;top:270px;width:76px;height:72px;background:linear-gradient(135deg,var(--photo-warm),#cdb9a3);"></div>
    <p class="abs body-copy" style="left:402px;top:354px;width:80px;">Brantley Homecare is a state-licensed private duty home health care agency serving the local community since 1996.</p>
  </section>

  <!-- INSIDE SPREAD -->
  <section class="spread spread--inside" aria-label="Brochure inside">
    <h1 class="abs headline">our nurses listen carefully to understand your needs</h1>
    <svg class="shape" style="left:240px;top:0" width="80" height="60" viewBox="0 0 80 60"><polygon points="0,0 80,0 80,60" fill="var(--green)"/></svg>
    <div class="abs" style="left:300px;top:0;width:80px;height:60px;background:var(--green);"></div>

    <div class="photo" role="img" aria-label="Photo of a nurse talking with an elderly woman on a sofa beside a plant" style="left:0;top:60px;width:380px;height:140px;background:linear-gradient(100deg,#dfe6d6,var(--photo-warm) 45%,var(--photo-skin) 75%,#e8e2d8);"></div>
    <div class="photo" role="img" aria-label="Photo of a caregiver's hands holding an elderly person's hand" style="left:382px;top:0;width:191px;height:200px;background:linear-gradient(135deg,#c4a187,var(--photo-skin) 55%,#e9dccf);"></div>
    <svg class="shape" style="left:533px;top:0" width="40" height="44" viewBox="0 0 40 44"><polygon points="0,0 40,0 40,44" fill="var(--pink)" opacity=".85"/></svg>

    <svg class="shape" style="left:0;top:205px" width="70" height="100" viewBox="0 0 70 100"><polygon points="70,0 70,100 0,50" fill="var(--green)"/><polygon points="70,0 0,50 0,0" fill="var(--cream)"/></svg>
    <svg class="shape" style="left:0;top:290px" width="120" height="108" viewBox="0 0 120 108"><polygon points="0,0 120,108 0,108" fill="var(--pink)"/><polygon points="0,0 70,0 120,108" fill="var(--cream)" opacity="0"/></svg>
    <div class="abs on-color" style="left:8px;top:340px;width:62px;">
      <p class="heading">LOREM IPSUM DOLOR SIT AMET</p>
      <p class="body-copy">Fusce aliquam, quam ut pulvinar scelerisque, justo mi mi, eget. Morbi hac nulla quisque euismod dolor mollis.</p>
    </div>

    <div class="abs column" style="left:76px;width:112px;">
      <p class="heading">LOREM IPSUM DOLOR SIT AMET</p>
      <p class="body-copy">Consectetur adipiscing elit. In eu hendrerit dolor. Nullam sodales nunc quis arcu dignissim interdum. Vivamus lobortis metus vel ligula euismod a pharetra mi pharetra.</p>
    </div>
    <div class="abs column" style="left:198px;width:176px;">
      <p class="heading">LOREM IPSUM DOLOR SIT AMET</p>
      <p class="body-copy">Consectetur adipiscing elit. In eu hendrerit dolor. Nullam sodales nunc quis arcu dignissim interdum. Vivamus lobortis metus vel ligula euismod a pharetra mi pharetra.</p>
      <p class="heading">LOREM IPSUM DOLOR SIT AMET</p>
      <p class="body-copy">Fusce aliquam, quam ut pulvinar scelerisque, justo mi mi, eget. Morbi hac nulla quisque euismod dolor mollis.</p>
      <p class="heading">LOREM IPSUM DOLOR SIT AMET</p>
      <p class="body-copy">Fusce aliquam, quam ut pulvinar scelerisque, justo mi mi, eget. Morbi hac nulla quisque euismod dolor mollis.</p>
    </div>
    <div class="abs column" style="left:390px;width:150px;">
      <p class="heading">LOREM IPSUM DOLOR SIT AMET</p>
      <p class="body-copy">Consectetur adipiscing elit. In eu hendrerit dolor. Nullam sodales nunc quis arcu dignissim interdum. Vivamus lobortis metus vel ligula euismod a pharetra mi pharetra.</p>
      <p class="heading">LOREM IPSUM DOLOR SIT AMET</p>
      <p class="body-copy" style="width:120px">Fusce aliquam, quam ut pulvinar scelerisque, justo mi mi, eget. Morbi hac nulla quisque euismod dolor mollis.</p>
      <p class="heading">LOREM IPSUM DOLOR SIT AMET</p>
      <p class="body-copy" style="width:120px">Fusce aliquam, quam ut pulvinar scelerisque, justo mi mi, eget. Morbi hac nulla quisque euismod dolor mollis.</p>
    </div>
    <svg class="shape" style="left:518px;top:310px" width="55" height="88" viewBox="0 0 55 88"><polygon points="55,0 55,55 0,28" fill="var(--green)"/><polygon points="55,40 55,88 10,88" fill="var(--pink)" opacity=".85"/></svg>
  </section>

</div>
</body>
</html>
```